Business Card Design for LeafCrest (Farming Devices)

We need Business Cards for our new Company based in Switzerland called "LeafCrest" We develop innovativ products for indoor and outdoor Farming for household and components for vertical farming. Our initial BloomNest gives people the possibility to grow their own food at home all year round. The design should communicate freshness, innovation, health.

```html
<!DOCTYPE html>
<html lang="en">
<head>
<meta charset="utf-8">
<title>LeafCrest Business Card</title>
<link rel="stylesheet" href="https://fonts.googleapis.com/css2?family=Montserrat:ital,wght@0,400;0,500;0,600;0,800;1,400&display=swap">
<style>
  :root {
    --bg: #8c8c8c;
    --card: #ffffff;
    --green: #74b243;
    --blue: #176fba;
    --ink: #1c1c1c;
  }
  * { box-sizing: border-box; margin: 0; padding: 0; }
  html, body {
    width: 1200px; height: 1017px; overflow: hidden;
    background: var(--bg);
    font-family: "Montserrat", Arial, sans-serif;
  }
  .card {
    position: absolute; left: 250px;
    width: 700px; height: 400px;
    background: var(--card);
    box-shadow: 0 6px 18px rgba(0,0,0,.25);
    overflow: hidden;
  }
  .card--front { top: 92px; }
  .card--back { top: 525px; }

  /* front */
  .brand-name {
    position: absolute; left: 0; right: 0; top: 120px;
    text-align: center;
    font-weight: 800; font-size: 80px; letter-spacing: -1px;
    color: var(--green);
  }
  .web-row {
    position: absolute; left: 0; right: 0; top: 250px;
    display: flex; align-items: center; justify-content: center; gap: 22px;
  }
  .web-row .rule { width: 120px; height: 1px; background: var(--green); }
  .web-row .url {
    font-size: 17px; font-weight: 400; letter-spacing: 6px; color: var(--ink);
  }

  /* back */
  .holder { position: absolute; left: 56px; top: 70px; }
  .holder-name {
    font-weight: 800; font-size: 40px; color: var(--blue); letter-spacing: 1px;
  }
  .holder-role {
    font-style: italic; font-size: 22px; color: var(--ink); margin-top: 2px;
  }
  .contacts {
    position: absolute; left: 56px; top: 228px;
    list-style: none; display: grid; gap: 10px;
  }
  .contacts li {
    display: flex; align-items: center; gap: 14px;
    font-size: 15px; color: var(--ink); line-height: 1.25;
  }
  .contacts .phone { font-weight: 600; font-size: 17px; }
  .icon {
    flex: none; width: 24px; height: 24px; border-radius: 50%;
    background: var(--green); display: grid; place-items: center;
  }
  .icon svg { width: 14px; height: 14px; }
  .tagline {
    position: absolute; right: 56px; top: 118px;
    text-align: right; font-weight: 800; font-size: 38px; line-height: 1.12;
    letter-spacing: .5px;
  }
  .tagline .lead { color: var(--green); display: block; }
  .tagline .rest { color: var(--blue); display: block; }
</style>
</head>
<body>

<section class="card card--front">
  <h1 class="brand-name">LeafCrest</h1>
  <div class="web-row">
    <span class="rule"></span>
    <span class="url">WWW.LEAFCREST.CO</span>
    <span class="rule"></span>
  </div>
</section>

<section class="card card--back">
  <div class="holder">
    <h2 class="holder-name">NAME HERE</h2>
    <p class="holder-role">Designation here</p>
  </div>

  <ul class="contacts">
    <li>
      <span class="icon"><svg viewBox="0 0 14 14"><path d="M7 1a4 4 0 0 0-4 4c0 3 4 8 4 8s4-5 4-8a4 4 0 0 0-4-4z" fill="#fff"/><circle cx="7" cy="5" r="1.4" fill="#74b243"/></svg></span>
      <span>123, Your address goes here,<br>Countrycode 0123456</span>
    </li>
    <li>
      <span class="icon"><svg viewBox="0 0 14 14"><path d="M3 1.5l2 .3 1 3-1.3 1a7 7 0 0 0 3.5 3.5l1-1.3 3 1 .3 2-1.5 1.5C6 12.5 1.5 8 1.5 3z" fill="#fff"/></svg></span>
      <span class="phone">0123 456 789</span>
    </li>
    <li>
      <span class="icon"><svg viewBox="0 0 14 14"><rect x="1.5" y="3" width="11" height="8" fill="#fff"/><path d="M1.5 3L7 7.5 12.5 3" fill="none" stroke="#74b243" stroke-width="1"/></svg></span>
      <span>info@leafcrest.com</span>
    </li>
    <li>
      <span class="icon"><svg viewBox="0 0 14 14" fill="none" stroke="#fff" stroke-width="1.1"><circle cx="7" cy="7" r="5.5"/><ellipse cx="7" cy="7" rx="2.4" ry="5.5"/><path d="M1.5 7h11M2.5 4h9M2.5 10h9"/></svg></span>
      <span>www.leafcrest.com</span>
    </li>
  </ul>

  <p class="tagline">
    <span class="lead">GROW YOUR</span>
    <span class="rest">OWN FOOD<br>AT HOME</span>
  </p>
</section>

</body>
</html>
```